Business cards for start-up accounting firm

I'm looking for a double sided business card ready for upload into Lumo print or similar print providers with no modification required by me.
I'm looking for something simple as i think cards that are too 'busy' actually detract from the message. I have some thoughts but more than happy to see what comes up. The logo i have came out of left field and i love it the moment i saw it!

My thoughts:

Side 1: Just the logo, perhaps on a dark grey or charcoal background to make the logo colours stand out?

Side 2: The call to action from me website 'Looking for a more relaxed, friendly and interactive relationship with your accountant?' with my contact information
Name: Gus Tarrow
Email: gus@ledgerowl.com.au
Website: www.ledgerowl.com.au
Phone: 1300 762 349

The call to action needs to be the first thing they see when they look at side 2. If it helps to know what we do and how we do it there is a draft website at www.ledgerowl.com.au

Like i said, happy to consider anything that comes up :)

Target Market(s)

i'm targeting small business owners who experience a lot of stress around finacial reporting and have had bad experiences with accountants in the past.

Industry/Entity Type

Accounting

Contact Information for Business Card

Contained in the Description

Font styles to use
Serif
Sans Serif
Other font styles liked:
• See logo files attached

Colors
474747

Requirements
Must have
• My logo, slogan and contact information

```html
<!DOCTYPE html>
<html lang="en">
<head>
<meta charset="utf-8">
<title>Ledger Owl — Business Card</title>
<link rel="stylesheet" href="https://fonts.googleapis.com/css2?family=Source+Sans+3:wght@400;600;700&display=swap">
<style>
  :root {
    --backdrop: #9b9b9b;
    --plum: #8f2e84;
    --plum-soft: #9a3c8f;
    --gold: #e4c41a;
    --paper: #f7f7f5;
    --ink: #1c1c1c;
    --white: #ffffff;
  }
  * { margin: 0; padding: 0; box-sizing: border-box; }
  html, body { width: 1200px; height: 800px; overflow: hidden; }
  body {
    background: var(--backdrop);
    font-family: "Source Sans 3", Arial, sans-serif;
    display: flex;
    align-items: center;
    justify-content: center;
    gap: 40px;
  }
  .card {
    position: relative;
    width: 540px;
    height: 309px;
    overflow: hidden;
    box-shadow: 0 6px 18px rgba(0,0,0,0.25);
  }

  /* Front side */
  .card--front { background: var(--plum); color: var(--white); }
  .front-watermark {
    position: absolute;
    left: 28px; top: 52px;
    font-size: 58px; font-weight: 700; line-height: 0.95;
    color: var(--plum-soft);
    text-transform: uppercase;
    letter-spacing: 1px;
  }
  .front-brand {
    position: absolute;
    right: 34px; top: 128px;
    text-align: right;
  }
  .brand-name {
    font-size: 40px; font-weight: 700; line-height: 1;
    text-transform: uppercase; letter-spacing: 1px;
    white-space: nowrap;
  }
  .brand-slogan {
    display: flex; align-items: center; gap: 8px;
    margin-top: 8px;
    font-size: 11px; letter-spacing: 2.5px; text-transform: uppercase;
    white-space: nowrap;
  }
  .brand-slogan::before { content: ""; width: 34px; height: 1px; background: currentColor; }
  .front-web {
    position: absolute; left: 34px; bottom: 30px;
    font-size: 16px; letter-spacing: 1px;
  }

  /* Back side */
  .card--back { background: var(--paper); color: var(--ink); }
  .back-brand { position: absolute; left: 30px; top: 70px; }
  .back-brand .brand-name { color: var(--gold); font-size: 32px; }
  .back-brand .brand-slogan { color: var(--plum); font-size: 8px; letter-spacing: 2px; gap: 6px; }
  .back-brand .brand-slogan::before { width: 26px; }
  .rule {
    position: absolute; left: 252px; right: 30px; top: 114px;
    height: 2px; background: var(--plum);
  }
  .holder-name {
    position: absolute; right: 40px; top: 78px;
    color: var(--plum); font-size: 24px; font-weight: 600;
  }
  .contact-list {
    position: absolute; left: 34px; bottom: 34px;
    list-style: none;
  }
  .contact-item {
    display: flex; align-items: center; gap: 14px;
    font-size: 17px; line-height: 28px;
  }
  .contact-icon { width: 16px; height: 16px; fill: var(--plum); }
</style>
</head>
<body>
  <section class="card card--front" aria-label="Card front">
    <div class="front-watermark" aria-hidden="true">Ledger<br>Owl</div>
    <div class="front-brand">
      <div class="brand-name">Ledger Owl</div>
      <div class="brand-slogan">Calm books, clear growth</div>
    </div>
    <div class="front-web">www.ledgerowl.com.au</div>
  </section>

  <section class="card card--back" aria-label="Card back">
    <div class="back-brand">
      <div class="brand-name">Ledger Owl</div>
      <div class="brand-slogan">Calm books, clear growth</div>
    </div>
    <div class="holder-name">Gus Tarrow</div>
    <div class="rule"></div>
    <ul class="contact-list">
      <li class="contact-item">
        <svg class="contact-icon" viewBox="0 0 16 16" aria-hidden="true"><path d="M3 1h3l1 4-2 1a8 8 0 0 0 5 5l1-2 4 1v3c0 1-1 2-2 2A13 13 0 0 1 1 3c0-1 1-2 2-2z"/></svg>
        1300 762 349
      </li>
      <li class="contact-item">
        <svg class="contact-icon" viewBox="0 0 16 16" aria-hidden="true"><path d="M1 3h14v10H1z M2 4l6 5 6-5" fill="none" stroke="#8f2e84" stroke-width="1.6"/></svg>
        gus@ledgerowl.com.au
      </li>
      <li class="contact-item">
        <svg class="contact-icon" viewBox="0 0 16 16" aria-hidden="true"><circle cx="8" cy="8" r="7" fill="none" stroke="#8f2e84" stroke-width="1.6"/><path d="M1 8h14M8 1c-3 4-3 10 0 14M8 1c3 4 3 10 0 14" fill="none" stroke="#8f2e84" stroke-width="1.2"/></svg>
        www.ledgerowl.com.au
      </li>
    </ul>
  </section>
</body>
</html>
```